Your After-Split Lantern: Sensible, Everyday Guidance for the Freshly Solo

I need a wraparound book cover design for a ~132-page workbook. Trim size will be 8.5x11 and the book will be on 60# paper. The name of this project is the name and subtitle of the book. Here's the synopsis I've come up with, which should be included on the back cover (without the quote marks):
"So you're divorced. What do you do now? There are probably a whole bunch of
things you never thought of, like:
- Cleaning up and automating your finances
- Making sure your insurance coverages are all correct
- Removing your former spouse's name from your assets and liabilities
- Building your personal team of financial advisors
Are you aware you need to take care of these things, but you don't know where to
start? This workbook is perfect for you. You'll be led, step by step, through detailed
explanations of how to do everything on this list, and much, much more!"
Here's the author bio for the back cover:
"Gregory T. Whitlock, Esq. graduated from Halvern College School of Law in 2002 and has been a practicing trial lawyer in the Metro Atlanta area ever since. Family law has always been a big part of Greg's practice. Throughout his career, Greg has helped hundreds of people through their divorce cases, and now through this book, Greg looks forward to being able to help them after the dust settles."
I have an ISBN bar code ready to go, so leave space for it on the back cover in the bottom right corner (winner will be expected to add the bar code graphic to the finished product).
This will be a print-on-demand book through Brindlemart's PressNook. They have a sizing template if you want to grab it for yourself.
Target Market(s)
Primarily divorced women, especially middle-aged and older
Look and feel
Each slider illustrates characteristics of the customer's brand and the style your logo design should communicate.

```html
<!DOCTYPE html>
<html lang="en">
<head>
<meta charset="utf-8">
<title>Your After-Split Lantern – Wraparound Cover</title>
<link rel="stylesheet" href="https://fonts.googleapis.com/css2?family=Anton&family=Crimson+Text:wght@400;600&family=Oswald:wght@700&display=swap">
<style>
  :root {
    --cover-red: #b01622;
    --heading-red: #b3121e;
    --ink: #141414;
    --body-ink: #1e1e1e;
    --paper-top: #ffffff;
    --paper-bottom: #e2ebe8;
    --white: #ffffff;
  }
  * { margin: 0; padding: 0; box-sizing: border-box; }
  html, body { width: 1200px; height: 776px; overflow: hidden; background: var(--white); }
  .cover {
    position: relative;
    width: 1200px;
    height: 776px;
    overflow: hidden;
    background: linear-gradient(180deg, var(--paper-top) 0%, #f3f7f6 45%, var(--paper-bottom) 100%);
    font-family: "Crimson Text", Georgia, serif;
    color: var(--body-ink);
  }

  /* Back cover */
  .back { position: absolute; left: 0; top: 0; width: 576px; height: 776px; }
  .synopsis-lead {
    position: absolute; left: 30px; top: 36px; width: 516px;
    text-align: center; color: var(--heading-red);
    font-weight: 600; font-size: 18px; line-height: 26px; letter-spacing: 0.4px;
    text-transform: uppercase;
  }
  .synopsis {
    position: absolute; left: 47px; top: 118px; width: 456px;
    font-size: 16.4px; line-height: 22.6px; text-align: justify;
  }
  .synopsis ul { list-style: none; }
  .about-band {
    position: absolute; left: 0; top: 356px; width: 576px; height: 49px;
    background: var(--cover-red); color: var(--white);
    font-family: "Oswald", "Anton", sans-serif; font-weight: 700;
    font-size: 37px; line-height: 49px; text-align: center; letter-spacing: 0.5px;
    padding-right: 26px;
  }
  .bio {
    position: absolute; left: 47px; top: 414px; width: 456px;
    font-size: 16.4px; line-height: 22.6px; text-align: justify;
  }
  .barcode-space {
    position: absolute; left: 336px; top: 630px; width: 164px; height: 101px;
    background: var(--white);
  }

  /* Spine */
  .spine {
    position: absolute; left: 576px; top: 0; width: 47px; height: 776px;
    background: var(--cover-red);
  }
  .spine-title {
    position: absolute; left: 23.5px; top: 28px;
    transform-origin: 0 0; transform: rotate(90deg) translateY(-50%);
    white-space: nowrap; color: var(--white);
    font-family: "Oswald", sans-serif; font-weight: 700;
    font-size: 21px; letter-spacing: 5.2px;
  }
  .spine-author {
    position: absolute; left: 23.5px; top: 440px;
    transform-origin: 0 0; transform: rotate(90deg) translateY(-50%);
    white-space: nowrap; color: var(--white);
    font-size: 29px; letter-spacing: 0.3px;
  }

  /* Front cover */
  .front { position: absolute; left: 623px; top: 0; width: 577px; height: 776px; }
  .hero-photo {
    position: absolute; left: 0; top: 0; width: 577px; height: 461px;
    background:
      radial-gradient(ellipse 38% 42% at 50% 22%, #e8c9a8 0%, rgba(232,201,168,0) 100%),
      radial-gradient(ellipse 26% 24% at 48% 66%, #c8242a 0%, rgba(200,36,42,0) 100%),
      linear-gradient(180deg, #dcebf0 0%, #eef3f4 45%, #f0dde2 100%);
  }
  .tagline-band {
    position: absolute; left: 0; top: 461px; width: 577px; height: 27px;
    background: var(--cover-red); color: var(--white);
    font-size: 15.6px; line-height: 27px; text-align: center; letter-spacing: 0.6px;
    text-transform: uppercase; font-weight: 600;
  }
  .title { position: absolute; left: 0; top: 0; width: 577px; }
  .title-your {
    position: absolute; left: 60px; top: 588px;
    transform-origin: 0 0; transform: rotate(-90deg);
    color: var(--cover-red); font-family: "Anton", sans-serif;
    font-size: 26px; line-height: 26px; letter-spacing: 0.5px;
  }
  .title-main {
    position: absolute; left: 86px; top: 502px;
    font-family: "Anton", sans-serif; color: var(--ink);
    font-size: 86px; line-height: 94px; letter-spacing: 1px; white-space: nowrap;
  }
  .title-sub {
    position: absolute; left: 104px; top: 592px; width: 434px;
    font-family: "Anton", sans-serif; color: var(--ink);
    font-size: 84px; line-height: 90px; letter-spacing: 19px; white-space: nowrap;
  }
  .front-author {
    position: absolute; left: 0; top: 708px; width: 577px; text-align: center;
    font-size: 38px; line-height: 44px; color: var(--ink); padding-left: 18px;
  }
</style>
</head>
<body>
<main class="cover">
  <section class="back">
    <h2 class="synopsis-lead">So you're divorced. What do you do now?<br>There are probably a whole bunch of<br>things you never thought of, like:</h2>
    <div class="synopsis">
      <ul>
        <li>- Cleaning up and automating your finances</li>
        <li>- Making sure your insurance coverages are all correct</li>
        <li>- Removing your former spouse's name from your assets and liabilities.</li>
        <li>- Building your personal team of financial advisors</li>
      </ul>
      <p>Are you aware you need to take care of these things, but you don't know where to start? This workbook is perfect for you. You'll be led, step by step, through detailed explanations of how to do everything on this list, and much, much more.</p>
    </div>
    <h2 class="about-band">ABOUT THE AUTHOR</h2>
    <p class="bio">Gregory T. Whitlock, Esq. graduated from Halvern College School of Law in 2002 and has been a practicing trial lawyer in the Metro Atlanta area ever since. Family law has always been a big part of Greg's practice. Throughout his career, Greg has helped hundreds of people through their divorce cases, and now through this book, Greg looks forward to being able to help them after the dust settles.</p>
    <div class="barcode-space" aria-label="Space reserved for ISBN barcode"></div>
  </section>

  <section class="spine">
    <span class="spine-title">YOUR AFTER-SPLIT LANTERN</span>
    <span class="spine-author">Gregory T. Whitlock</span>
  </section>

  <section class="front">
    <div class="hero-photo" role="img" aria-label="Photo of a woman holding two halves of a torn red paper heart"></div>
    <p class="tagline-band">Sensible, Everyday Guidance for the Freshly Solo</p>
    <h1 class="title">
      <span class="title-your">YOUR</span>
      <span class="title-main">AFTER-SPLIT</span>
      <span class="title-sub">LANTERN</span>
    </h1>
    <p class="front-author">Gregory T. Whitlock</p>
  </section>
</main>
</body>
</html>
```